New School header and footer

Our school needs a modern new header and a matching footer. Currently we have the school logo, name and contact with no graphics at all (attached).
I have also attached another version of the school logo which is on our school sign.
The school's logo is a Swift (Apus pacificus) (bird) see http://www.findlyweb.example/search?q=swift+bird+images

The school is located in North Queensland Australia near the town of Ingham it was established in 1922

I would like the header/footer to have:
The school name- Marrelda State School
School moto - Courage beside kindness
contact details: Address Phone Fax website and principal email (some of these things could be in the footer) these details are in the uploaded files
The logo or elements of the logo (as is or modified to modernise)

School website is https://marreldass.qlx.edu.example

The header and footer would be used on A4 paper with microsoft word it will be used for the school newsletter and in all official school documents.

It can be colour or black and white. School uniforms are have light blue some dark blue and white the colours in the design are not limited to these colours.
Updates

Thanks to those people who have already submitted designs. I have made some additions to the brief in the should have and should not have sections and also the sliding scale thing. I hope that helps.

There are a lot of designs thankyou all so much. Some feedback from my staff is that we really need to keep the traditional logo of the bird from the website. It doesn't have to have the words around it but the shape and position needs to stay the same. I thought we were ready to change modernise the logo but unfortunately they aren't ready. However the rest of the design needs to be modern, less rigid and square. There is one square design that I did like and they have made the changes required. I will choose the designs I like and should be putting them up for online voting next week.
Just a side note a large tropical cyclone is moving close to our community. We are not at risk right now but it is possible that we will experience flooding and maybe loss of power so if there is a delay in posting the results this will probably be the reason.  I will try to respond to last minute questions or design submissions but I'll be pretty busy preparing my home and the school for the possibility of this weather event. Once again thankyou for your submissions I have been impressed by the quailty of the submissions from this particular design crowd.

Target Market(s)

For a school used in official documents, letters, and newsletters.

My staff will be choosing the winner.

Industry/Entity Type

School

Requirements
Must have
• School name
School motto
Address
Phone
Fax
Website URL
Header and footer
Should not have
• Avoid large amounts of block colours this letter head will be used in colour format most of the time but will be photo copied and faxed from time to time.

```html
<!DOCTYPE html>
<html lang="en">
<head>
<meta charset="utf-8">
<title>Marrelda State School Letterhead</title>
<link rel="stylesheet" href="https://fonts.googleapis.com/css2?family=Tinos:wght@700&family=PT+Sans:wght@400&display=swap">
<style>
  :root {
    --backdrop: #ece9e4;
    --paper: #ffffff;
    --navy: #1d3f8a;
    --rule: #2a4f9a;
    --footer-blue: #1f4fa0;
    --band-light: #e8f0fb;
    --band-mid: #a9c8f0;
    --band-deep: #4a8fe0;
    --ghost: #f2f2f2;
    --ghost-text: #ebebeb;
  }
  html, body {
    margin: 0;
    padding: 0;
    width: 1105px;
    height: 1200px;
    overflow: hidden;
    background: var(--backdrop);
  }
  .letterhead {
    position: absolute;
    left: 162px;
    top: 48px;
    width: 780px;
    height: 1103px;
    background: var(--paper);
    box-shadow: 0 2px 10px rgba(0,0,0,0.18);
    overflow: hidden;
  }
  .side-band {
    position: absolute;
    left: 0;
    top: 0;
    width: 60px;
    height: 1103px;
  }
  .school-name {
    position: absolute;
    left: 66px;
    top: 20px;
    margin: 0;
    font-family: "Tinos", "Times New Roman", serif;
    font-weight: 700;
    font-size: 28px;
    letter-spacing: 0.3px;
    color: var(--navy);
    text-transform: uppercase;
  }
  .school-motto {
    position: absolute;
    left: 68px;
    top: 52px;
    margin: 0;
    font-family: "PT Sans", Arial, sans-serif;
    font-size: 23px;
    color: var(--navy);
    text-transform: uppercase;
  }
  .header-rule {
    position: absolute;
    left: 26px;
    top: 92px;
    width: 721px;
    height: 2px;
    background: var(--rule);
  }
  .crest-mark {
    position: absolute;
    left: 150px;
    top: 330px;
    width: 540px;
    height: 540px;
  }
  .crest-name {
    position: absolute;
    left: 150px;
    top: 578px;
    width: 540px;
    text-align: center;
    font-family: "PT Sans", Arial, sans-serif;
    font-size: 40px;
    letter-spacing: 3px;
    color: var(--ghost-text);
    text-transform: uppercase;
  }
  .footer-rule {
    position: absolute;
    left: 57px;
    top: 1034px;
    width: 692px;
    height: 2px;
    background: var(--rule);
  }
  .footer-block {
    position: absolute;
    top: 1044px;
    margin: 0;
    font-family: "Tinos", "Times New Roman", serif;
    font-weight: 700;
    font-size: 12px;
    line-height: 13px;
    color: var(--footer-blue);
    font-style: normal;
  }
  .footer-address { left: 90px; }
  .footer-contact { left: 462px; }
  .footer-contact .label {
    display: inline-block;
    width: 52px;
  }
</style>
</head>
<body>
  <main class="letterhead">
    <svg class="side-band" width="60" height="1103" viewBox="0 0 60 1103" aria-hidden="true">
      <defs>
        <linearGradient id="bandFade" x1="0" y1="0" x2="0" y2="1">
          <stop offset="0" stop-color="var(--band-light)"/>
          <stop offset="0.45" stop-color="var(--band-mid)"/>
          <stop offset="1" stop-color="var(--band-deep)"/>
        </linearGradient>
      </defs>
      <polygon points="0,0 26,0 26,472 57,566 57,1103 0,1103" fill="url(#bandFade)"/>
    </svg>

    <header>
      <h1 class="school-name">Marrelda State School</h1>
      <p class="school-motto">Courage beside kindness</p>
      <div class="header-rule"></div>
    </header>

    <svg class="crest-mark" width="540" height="540" viewBox="0 0 540 540" role="img" aria-label="Faint school crest watermark: swift in flight ringed by the school name">
      <circle cx="270" cy="270" r="262" fill="var(--ghost)"/>
    </svg>
    <div class="crest-name">Marrelda State School</div>

    <footer>
      <div class="footer-rule"></div>
      <address class="footer-block footer-address">
        Carrow Highway<br>
        Marrelda 4861<br>
        PO BOX 512 WENDALE 4861
      </address>
      <address class="footer-block footer-contact">
        <span class="label">Phone:</span>4700 0124<br>
        <span class="label">Fax:</span>4700 0121<br>
        e-mail: the.principal@marreldass.qlx.edu.example<br>
        <span class="label">Web:</span>https://marreldass.qlx.edu.example
      </address>
    </footer>
  </main>
</body>
</html>
```